Design a Unique and Eye-Catching Necklace Card for Verandelle's New Lumenwave Line

Attention all creative minds from around the world! Verandelle, a company known for its free-spirited and bohemian chic vibe, is proud to announce a new design contest. We are inviting you to create a dynamic and unique necklace card for our upcoming Lumenwave line.

Our new Lumenwave line comprises 12-20 unique necklace combinations. Each necklace features different stones, each with its own healing properties and associated zodiac sign. We are looking for a template that can be easily modified to change the names of the stones, zodiac sign, and the colors to match the specific stones on each necklace.

The card should be 3 x 4,
It should include the names of the stones, the associated zodiac sign (if applicable), a few words about the healing properties of the stones, and a captivating graphic that represents the colors of the stones.

Our goal is to delight our customers with packaging as unique as the necklaces themselves. The necklace should be the focal point, but the text and graphic on the card should also draw the eye.

Please note that our target audience includes mid-priced boutiques across the country and festival-goers in Colorado. Your design should reflect the unique taste and free spirit of our clientele.

We are excited to see your creativity shine in this project. If there are any points that need clarification, please do not hesitate to ask. We look forward to your participation in bringing the Lumenwave line to life!
https://www.plorvex.example/board/QKTm_ZRwpe/u3hb9XKdLqWm72RtPoaVnc/edit?ref=QKTm_ZRwpe&src=share

https://www.plorvex.example/board/QKTr_BNyhwa/t8Ld-WsPzMEY246VqoXjNd/edit?ref=QKTr_BNyhwa&src=share
I want to use the flowing watercolor and have it change with each necklace color.
Use the necklaces below. Incorporate the zodiac symbol as is shown below.

Examples of other cards in our collection

The Little Pebble Pendant: https://www.plorvex.example/board/QKTh_WomRtc/pbMRx63CKqnYs905Bd-aLe/edit?ref=QKTh_WomRtc&src=share

Other examples of necklace cards I like:

https://www.tindramart.example/item/731920584/green-emerald-stone-necklace-emerald?k=a1b2c3d4e5f60718293a4b5c6d7e8f9012345678&s=7d3e91ab

https://www.tindramart.example/item/846201937/january-birthstone-necklace-green-garnet?k=b2c3d4e5f60718293a4b5c6d7e8f901234567890&s=4c82fe10

https://www.tindramart.example/item/2093748165/natural-crystal-bracelets-empath?k=c3d4e5f60718293a4b5c6d7e8f90123456789012&s=9ab0c37d

https://www.tindramart.example/item/2174603958/black-obsidian-protection-necklace-black?k=d4e5f60718293a4b5c6d7e8f9012345678901234&s=e15d6b28

Target Market(s)

Women aged 25-50 with a spiritual, hippy, bohemain, yoga vibe.

Industry/Entity Type

Handmade Jewelry | Wholesale jewelry | Retail Jewelry sales at Festivals

Font styles to use
Script

Colors

Designer to choose colors to be used in the design.

Requirements
Must have
• A template that can be interchangable with the stone colors, names and healing properties.
Nice to have
• Some different ideas about the graphic color patterns on the card.
Should not have
• Any graphic that would cover the middle of the necklace card and keep people from seeing the neckalce

```html
<!DOCTYPE html>
<html lang="en">
<head>
<meta charset="utf-8">
<title>Lumenwave Necklace Cards</title>
<link rel="stylesheet" href="https://fonts.googleapis.com/css2?family=Cinzel:wght@400;500&family=Outfit:wght@300;400&display=swap">
<style>
  :root {
    --page: #ffffff;
    --card-bg: #fafbfd;
    --aqua-ink: #1d3fc4;
    --aqua-tint: #8fb0f5;
    --chryso-ink: #4aa9a0;
    --chryso-tint: #6fe3a0;
    --fluor-ink: #9b4a9e;
    --fluor-tint: #d79af0;
    --jasper-ink: #2c5a4c;
    --jasper-tint: #f2a6a6;
    --jasper-tint-2: #a8d28a;
  }
  * { box-sizing: border-box; margin: 0; padding: 0; }
  html, body { width: 1200px; height: 1190px; overflow: hidden; background: var(--page); }
  .card-grid {
    position: relative;
    width: 1200px; height: 1190px;
    display: grid;
    grid-template-columns: 560px 560px;
    grid-template-rows: 555px 555px;
    column-gap: 24px; row-gap: 22px;
    padding: 26px 0 0 26px;
  }
  .card {
    position: relative;
    overflow: hidden;
    background: var(--card-bg);
    color: var(--ink);
  }
  .card--aqua { --ink: var(--aqua-ink); --tint: var(--aqua-tint); --tint-2: var(--aqua-tint); }
  .card--chryso { --ink: var(--chryso-ink); --tint: var(--chryso-tint); --tint-2: var(--chryso-tint); }
  .card--fluor { --ink: var(--fluor-ink); --tint: var(--fluor-tint); --tint-2: var(--fluor-tint); }
  .card--jasper { --ink: var(--jasper-ink); --tint: var(--jasper-tint); --tint-2: var(--jasper-tint-2); }

  .crystal-field {
    position: absolute; left: 0; right: 0; bottom: 0; height: 178px;
    background:
      linear-gradient(180deg, var(--card-bg) 0%, rgba(250,251,253,0) 45%),
      linear-gradient(90deg, var(--tint) 0%, rgba(255,255,255,0.4) 50%, var(--tint-2) 100%);
    opacity: 0.85;
  }
  .necklace {
    position: absolute; left: 0; top: 150px; width: 560px; height: 160px;
  }
  .card--jasper .necklace { top: 0; height: 330px; }

  .stone-name {
    position: absolute; left: 0; right: 0; top: 42px;
    text-align: center;
    font-family: "Cinzel", serif;
    font-weight: 500;
    font-size: 32px;
    letter-spacing: -0.5px;
    color: var(--ink);
    z-index: 2;
  }
  .card--jasper .stone-name { top: 34px; color: var(--jasper-ink); }

  .zodiac {
    position: absolute; left: 50%; top: 135px; transform: translateX(-50%);
    display: flex; flex-direction: column; align-items: center; gap: 6px;
    z-index: 2;
  }
  .zodiac-label {
    font-family: "Outfit", sans-serif; font-weight: 400;
    font-size: 12.5px; letter-spacing: 2.5px; color: var(--ink);
  }
  .zodiac-badge {
    width: 54px; height: 54px; border-radius: 50%;
    background: var(--ink); color: #fff;
    display: flex; align-items: center; justify-content: center;
    font-family: "Cinzel", serif; font-size: 28px; line-height: 1;
  }
  .benefit {
    position: absolute; left: 0; right: 0; top: 356px;
    text-align: center;
    font-family: "Outfit", sans-serif; font-weight: 300;
    font-size: 26px; line-height: 1.1; letter-spacing: -0.3px;
    color: var(--ink);
    z-index: 2;
  }
  .card--chryso .benefit { top: 356px; }
  .card--jasper .benefit { top: 356px; }
</style>
</head>
<body>
<main class="card-grid">

  <section class="card card--aqua">
    <div class="crystal-field" role="img" aria-label="Faceted crystal pattern in soft blues"></div>
    <svg class="necklace" viewBox="0 0 560 160" role="img" aria-label="Photo of an aquamarine and kyanite bead necklace on a fine silver chain">
      <defs>
        <linearGradient id="g-aqua" x1="0" x2="1">
          <stop offset="0" stop-color="#3f78d8"/><stop offset="0.5" stop-color="#a9cde0"/><stop offset="1" stop-color="#3f78d8"/>
        </linearGradient>
      </defs>
      <path d="M0 32 Q280 160 560 32" fill="none" stroke="#c9ccd2" stroke-width="1.5"/>
      <path d="M40 65 Q280 190 520 65" fill="none" stroke="url(#g-aqua)" stroke-width="28" stroke-linecap="round" opacity="0.85"/>
    </svg>
    <h2 class="stone-name">Aquamarine &amp; Kyanite</h2>
    <div class="zodiac"><span class="zodiac-label">PISCES</span><span class="zodiac-badge">&#9802;&#xFE0E;</span></div>
    <p class="benefit">Reduce Stress &amp; Anxiety</p>
  </section>

  <section class="card card--chryso">
    <div class="crystal-field" role="img" aria-label="Faceted crystal pattern in soft greens"></div>
    <svg class="necklace" viewBox="0 0 560 160" role="img" aria-label="Photo of a chrysocolla and aquamarine bead necklace on a fine silver chain">
      <defs>
        <linearGradient id="g-chryso" x1="0" x2="1">
          <stop offset="0" stop-color="#2b6f6a"/><stop offset="0.5" stop-color="#1f8a8a"/><stop offset="1" stop-color="#3b5c55"/>
        </linearGradient>
      </defs>
      <path d="M0 30 Q280 180 560 30" fill="none" stroke="#c9ccd2" stroke-width="1.5"/>
      <path d="M60 72 Q280 210 500 72" fill="none" stroke="url(#g-chryso)" stroke-width="28" stroke-linecap="round" opacity="0.85"/>
    </svg>
    <h2 class="stone-name">Chrysocolla &amp; Aquamarine</h2>
    <div class="zodiac"><span class="zodiac-label">VIRGO</span><span class="zodiac-badge">&#9805;&#xFE0E;</span></div>
    <p class="benefit">Detoxifies the liver,<br>kidneys, and intestines.</p>
  </section>

  <section class="card card--fluor">
    <div class="crystal-field" role="img" aria-label="Faceted crystal pattern in soft violets"></div>
    <svg class="necklace" viewBox="0 0 560 160" role="img" aria-label="Photo of a fluorite bead necklace on a fine silver chain">
      <defs>
        <linearGradient id="g-fluor" x1="0" x2="1">
          <stop offset="0" stop-color="#d8c0ee"/><stop offset="0.5" stop-color="#8a2b6a"/><stop offset="1" stop-color="#b8b0c0"/>
        </linearGradient>
      </defs>
      <path d="M0 65 Q280 160 560 65" fill="none" stroke="#c9ccd2" stroke-width="1.5"/>
      <path d="M55 100 Q280 190 505 100" fill="none" stroke="url(#g-fluor)" stroke-width="28" stroke-linecap="round" opacity="0.85"/>
    </svg>
    <h2 class="stone-name">Fluorite</h2>
    <div class="zodiac"><span class="zodiac-label">PISCES</span><span class="zodiac-badge">&#9802;&#xFE0E;</span></div>
    <p class="benefit">Improves decision making</p>
  </section>

  <section class="card card--jasper">
    <div class="crystal-field" role="img" aria-label="Faceted crystal pattern in soft pinks and greens"></div>
    <svg class="necklace" viewBox="0 0 560 330" role="img" aria-label="Photo of an ocean jasper bead necklace on a fine silver chain">
      <defs>
        <linearGradient id="g-jasper" x1="0" x2="1">
          <stop offset="0" stop-color="#2e6b5c"/><stop offset="0.45" stop-color="#d8c8b0"/><stop offset="0.7" stop-color="#c86a2a"/><stop offset="1" stop-color="#e89aa4"/>
        </linearGradient>
      </defs>
      <path d="M38 0 L80 120 M532 0 L500 110" fill="none" stroke="#c9ccd2" stroke-width="1.5"/>
      <path d="M80 130 Q110 300 290 305 Q470 300 490 130" fill="none" stroke="url(#g-jasper)" stroke-width="36" stroke-linecap="round" opacity="0.85"/>
    </svg>
    <h2 class="stone-name">Ocean Jasper</h2>
    <p class="benefit">Alleviates depression &amp; stress</p>
  </section>

</main>
</body>
</html>
```